Specialist Doctor Personal Website

I wanted a website:
1. In my name
2. Describing my scope of practice
3. Having my photo
4. Has links to the places I work at
5. Provides patient information
6. Provides an email for contact

Target Market(s)

Victorian patients and GPs

Industry/Entity Type

Health

Coding

Coded - Design and coding required

Number of Pages Required

1 page

Font styles to use
Script

Colors
0054AA
0677BA
7BADD7
CADEEF
E8F1F8
6B429C
8869AF
B7A5CE
E3DAEB
F3F0F8

Requirements
Must have
• Modern design
Nice to have
• Links to email/fax/linkedin

```html
<!DOCTYPE html>
<html lang="en">
<head>
<meta charset="utf-8">
<title>Avery Lane – Specialist Doctor</title>
<link href="https://fonts.googleapis.com/css2?family=Roboto:wght@400;500;700&display=swap" rel="stylesheet">
<style>
:root{
  --blue:#0054AA;
  --blue-2:#0677BA;
  --blue-light:#7BADD7;
  --purple:#6B429C;
  --purple-2:#8869AF;
  --text:#5a5a5a;
  --ink:#222;
  --white:#fff;
}
*{margin:0;padding:0;box-sizing:border-box}
html,body{width:1200px;height:2895px;overflow:hidden;background:var(--white);font-family:'Roboto',sans-serif}
a{text-decoration:none}
.page{position:relative;width:1200px;height:2895px;overflow:hidden}

/* header */
.site-header{position:absolute;left:0;top:0;width:1200px;height:73px;background:var(--white)}
.brand{position:absolute;left:99px;top:9px;width:138px;height:138px;border-radius:50%;background:var(--white);z-index:5;display:flex;align-items:center;justify-content:center}
.brand-name{font-size:19px;font-weight:500;color:var(--blue);text-align:center;line-height:1.1}
.nav a{position:absolute;top:29px;font-size:14px;color:var(--ink)}
.nav a.active{color:var(--purple)}
.pill{position:absolute;display:flex;align-items:center;justify-content:center;gap:6px;border-radius:20px;color:var(--white);font-size:13.5px;font-weight:700}
.pill svg{width:13px;height:13px;fill:currentColor}
.pill-email{left:693px;top:20px;width:217px;height:36px;background:var(--blue)}
.pill-phone{left:916px;top:20px;width:172px;height:36px;background:var(--purple)}

/* hero */
.hero{position:absolute;left:0;top:73px;width:1200px;height:600px;background:linear-gradient(135deg,#0b4fb0 0%,var(--blue) 60%,#0a4aa6 100%)}
.hero-bubble{position:absolute;left:54px;top:144px;width:296px;height:296px;border-radius:50%;background:var(--purple)}
.hero-kicker{position:absolute;left:111px;top:190px;font-size:21px;font-weight:500;color:var(--white)}
.hero-title{position:absolute;left:108px;top:220px;font-size:47px;font-weight:500;color:var(--white);white-space:nowrap}
.hero-lead{position:absolute;left:111px;top:286px;width:370px;font-size:15px;line-height:21.5px;color:var(--white)}
.hero-call{position:absolute;left:108px;top:360px;width:173px;height:38px;border:1.5px solid var(--white);border-radius:20px;background:transparent}
.dots{position:absolute;left:109px;top:537px;display:flex;gap:7px}
.dots span{width:11px;height:11px;border-radius:50%;border:1.5px solid var(--white)}
.dots span.on{background:var(--white)}
.portrait-back{position:absolute;left:565px;top:90px;width:506px;height:643px;background:var(--purple);border-radius:4px}
.portrait{position:absolute;left:583px;top:73px;width:505px;height:643px;border-radius:4px;background:linear-gradient(180deg,#e6e7ea 0%,#cfd3da 45%,#1e3f86 75%,#18336f 100%)}

/* about */
.about-crescent{position:absolute;left:111px;top:829px;width:410px;height:410px;border-radius:50%;background:linear-gradient(180deg,var(--blue) 0%,var(--purple) 100%)}
.about-photo{position:absolute;left:132px;top:833px;width:420px;height:420px;border-radius:50%;border:4px solid var(--white);background:radial-gradient(circle at 50% 40%,#9aa2a8 0%,#5c676e 50%,#1f2b2f 100%)}
.about-title{position:absolute;left:601px;top:826px;font-size:47px;font-weight:500;color:var(--blue)}
.about-title span{color:var(--purple)}
.copy{position:absolute;width:486px;font-size:15px;line-height:21.4px;color:var(--text);text-align:justify}
.copy p+p{margin-top:21.4px}
.btn{position:absolute;height:36px;border-radius:18px;background:var(--purple);color:var(--white);font-size:14px;font-weight:700;display:flex;align-items:center;justify-content:center;gap:5px}
.btn svg{width:12px;height:12px}

/* places */
.places-band{position:absolute;left:0;top:1352px;width:1200px;height:401px;background:linear-gradient(90deg,var(--purple) 0%,#3b4fae 55%,var(--blue) 100%)}
.places-title{position:absolute;left:0;top:1440px;width:1200px;text-align:center;font-size:49px;font-weight:500;color:var(--white)}
.place{position:absolute;top:1520px;width:231px;height:309px}
.place-img{width:231px;height:309px}
.place-label{position:absolute;left:25px;top:287px;width:182px;height:47px;background:var(--blue);color:var(--white);font-size:14.5px;font-weight:700;display:flex;align-items:center;justify-content:center}

/* patient */
.patient-title{position:absolute;left:108px;top:1948px;font-size:49px;font-weight:500;color:var(--blue)}
.patient-title span{color:var(--purple)}
.patient-circle{position:absolute;left:730px;top:2023px;width:292px;height:292px;border-radius:50%;background:var(--purple)}
.patient-img-a{position:absolute;left:628px;top:1957px;width:336px;height:310px;background:linear-gradient(135deg,#e9e4dc 0%,#d9c9b4 45%,#f2b97f 70%,#8a9fb3 100%)}
.patient-img-b{position:absolute;left:886px;top:2160px;width:202px;height:213px;border:3px solid var(--white);background:linear-gradient(160deg,#dfe3e6 0%,#b9c6d3 50%,#6f86a3 100%)}

/* footer */
.site-footer{position:absolute;left:0;top:2477px;width:1200px;height:418px;background:var(--blue);color:var(--white)}
.foot-brand{position:absolute;left:111px;top:100px;width:116px;height:116px;border-radius:50%;border:2px solid var(--white);display:flex;align-items:center;justify-content:center;font-size:17px;font-weight:500;text-align:center;line-height:1.1}
.foot-col{position:absolute;top:88px}
.foot-col h3{font-size:19.5px;font-weight:500;margin-bottom:18px;letter-spacing:.2px}
.foot-col a,.foot-col li{display:block;font-size:15px;line-height:21.6px;color:var(--white);list-style:none}
.foot-col ul{list-style:none}
.contact li{position:relative;padding-left:41px}
.contact svg{position:absolute;left:0;top:5px;width:13px;height:13px;fill:var(--white)}
.copyright{position:absolute;left:0;top:316px;width:1200px;text-align:center;font-size:14.5px}
.social{position:absolute;left:584px;top:352px;width:32px;height:32px;border-radius:50%;background:var(--purple)}
</style>
</head>
<body>
<div class="page">

  <header class="site-header">
    <a class="brand" href="#"><span class="brand-name">Avery<br>Lane</span></a>
    <nav class="nav">
      <a class="active" href="#" style="left:297px">Home</a>
      <a href="#" style="left:361px">About me</a>
      <a href="#" style="left:447px">Services</a>
      <a href="#" style="left:527px">Work place</a>
      <a href="#" style="left:623px">Contact</a>
    </nav>
    <a class="pill pill-email" href="#"><svg viewBox="0 0 16 16"><path d="M1 3h14v1.2L8 9 1 4.2z M1 5.8l7 4.8 7-4.8V13H1z"/></svg>info@averylane.com</a>
    <a class="pill pill-phone" href="#"><svg viewBox="0 0 16 16"><path d="M3.6 1.2l2.3 2.6-1.4 2a8 8 0 0 0 5.7 5.7l2-1.4 2.6 2.3-1.3 2.3C7.3 14.6 1.4 8.7 1.3 2.5z"/></svg>+1 555 014 2738</a>
  </header>

  <section class="hero">
    <div class="hero-bubble"></div>
    <p class="hero-kicker">Welcome To</p>
    <h1 class="hero-title">Specialist Doctor</h1>
    <p class="hero-lead">Lorem ipsum dolor sit amet, consectetur adipiscing elit, sed do eiusmod tempor incididunt ut labore et dolore magna aliqua.</p>
    <a class="pill hero-call" href="#"><svg viewBox="0 0 16 16"><path d="M3.6 1.2l2.3 2.6-1.4 2a8 8 0 0 0 5.7 5.7l2-1.4 2.6 2.3-1.3 2.3C7.3 14.6 1.4 8.7 1.3 2.5z"/></svg>+1 555 014 2738</a>
    <div class="dots"><span class="on"></span><span></span><span></span><span></span></div>
  </section>
  <div class="portrait-back"></div>
  <div class="portrait" role="img" aria-label="Portrait photo of the doctor in a blue suit"></div>

  <section class="about">
    <div class="about-crescent"></div>
    <div class="about-photo" role="img" aria-label="Circular portrait photo of the doctor"></div>
    <h2 class="about-title">Hi, I’m <span>Avery Lane</span></h2>
    <div class="copy" style="left:602px;top:893px">
      <p>Lorem ipsum dolor sit amet, consectetur adipiscing elit, sed do eiusmod tempor incididunt ut labore et dolore magna aliqua. Ut enim ad minim veniam, quis nostrud exercitation ullamco laboris nisi ut aliquip ex ea commodo consequat. Duis aute irure dolor in reprehenderit in voluptate velit esse cillum dolore eu fugiat nulla pariatur.</p>
      <p>Excepteur sint occaecat cupidatat non proident, sunt in culpa qui officia deserunt mollit anim id est laborum. Lorem ipsum dolor sit amet, consectetur adipiscing elit, sed do eiusmod tempor incididunt ut labore et dolore magna aliqua. Ut enim ad minim veniam, quis nostrud exercitation ullamco laboris nisi ut aliquip ex ea commodo consequat. Duis aute irure dolor in reprehenderit in voluptate velit esse cillum dolore eu fugiat nulla pariatur. Excepteur sint occaecat cupidatat non proident, sunt in culpa qui officia deserunt mollit anim id est laborum.</p>
    </div>
    <a class="btn" href="#" style="left:603px;top:1214px;width:155px">LEARN MORE <svg viewBox="0 0 12 12"><circle cx="6" cy="6" r="6" fill="#fff"/><path d="M5 3l3 3-3 3" stroke="#6B429C" stroke-width="1.6" fill="none"/></svg></a>
  </section>

  <section class="places">
    <div class="places-band"></div>
    <h2 class="places-title">Places I Work</h2>
    <div class="place" style="left:111px"><div class="place-img" role="img" aria-label="City skyline at sunset" style="background:linear-gradient(180deg,#e9c9a6 0%,#b0683a 45%,#3b2a25 100%)"></div><a class="place-label" href="#">Lorem ipsum dolor</a></div>
    <div class="place" style="left:360px"><div class="place-img" role="img" aria-label="Office towers under a blue sky" style="background:linear-gradient(180deg,#4f9ed6 0%,#a9c9dc 40%,#5e7a55 75%,#3d4e3a 100%)"></div><a class="place-label" href="#">Lorem ipsum dolor</a></div>
    <div class="place" style="left:608px"><div class="place-img" role="img" aria-label="City skyline at night" style="background:linear-gradient(180deg,#1b1d3a 0%,#2a3a6e 45%,#7a3f52 75%,#d08a4a 100%)"></div><a class="place-label" href="#">Lorem ipsum dolor</a></div>
    <div class="place" style="left:857px"><div class="place-img" role="img" aria-label="Downtown skyline at dusk" style="background:linear-gradient(180deg,#9fb3cf 0%,#e3a57d 22%,#8c8f96 55%,#4c5562 100%)"></div><a class="place-label" href="#">Lorem ipsum dolor</a></div>
  </section>

  <section class="patient">
    <h2 class="patient-title">Patient <span>Information</span></h2>
    <div class="copy" style="left:109px;top:2017px">
      <p>Lorem ipsum dolor sit amet, consectetur adipiscing elit, sed do eiusmod tempor incididunt ut labore et dolore magna aliqua. Ut enim ad minim veniam, quis nostrud exercitation ullamco laboris nisi ut aliquip ex ea commodo consequat. Duis aute irure dolor in reprehenderit in voluptate velit esse cillum dolore eu fugiat nulla pariatur.</p>
      <p>Excepteur sint occaecat cupidatat non proident, sunt in culpa qui officia deserunt mollit anim id est laborum. Lorem ipsum dolor sit amet, consectetur adipiscing elit, sed do eiusmod tempor incididunt ut labore et dolore magna aliqua. Ut enim ad minim veniam, quis nostrud exercitation ullamco laboris nisi ut aliquip ex ea commodo consequat. Duis aute irure dolor in reprehenderit in voluptate velit esse cillum dolore eu fugiat nulla pariatur. Excepteur sint occaecat cupidatat non proident, sunt in culpa qui officia deserunt mollit anim id est laborum.</p>
    </div>
    <a class="btn" href="#" style="left:109px;top:2337px;width:156px">LEARN MORE <svg viewBox="0 0 12 12"><circle cx="6" cy="6" r="6" fill="#fff"/><path d="M5 3l3 3-3 3" stroke="#6B429C" stroke-width="1.6" fill="none"/></svg></a>
    <div class="patient-circle"></div>
    <div class="patient-img-a" role="img" aria-label="Patient talking with a doctor in a clinic"></div>
    <div class="patient-img-b" role="img" aria-label="Doctor consulting with a male patient"></div>
  </section>

  <footer class="site-footer">
    <div class="foot-brand">Avery<br>Lane</div>
    <div class="foot-col" style="left:390px">
      <h3>GENERAL</h3>
      <a href="#">Privacy Policy</a><a href="#">Terms of Use</a><a href="#">About Me</a><a href="#">Pricing</a><a href="#">Sign Up</a>
    </div>
    <div class="foot-col" style="left:630px">
      <h3>HELP</h3>
      <a href="#">Help</a><a href="#">FAQ</a><a href="#">Getting Started</a><a href="#">Features</a><a href="#">Support</a>
    </div>
    <div class="foot-col contact" style="left:862px">
      <h3>CONTACT</h3>
      <ul>
        <li><svg viewBox="0 0 16 16"><path d="M8 0a5 5 0 0 1 5 5c0 4-5 11-5 11S3 9 3 5a5 5 0 0 1 5-5zm0 3a2 2 0 1 0 0 4 2 2 0 0 0 0-4z"/></svg>Lorem ipsum dolor sit amet,<br>consectetur</li>
        <li><svg viewBox="0 0 16 16"><path d="M3.6 1.2l2.3 2.6-1.4 2a8 8 0 0 0 5.7 5.7l2-1.4 2.6 2.3-1.3 2.3C7.3 14.6 1.4 8.7 1.3 2.5z"/></svg>+1 555 014 273</li>
        <li><svg viewBox="0 0 16 16"><path d="M1 3h14v1.2L8 9 1 4.2z M1 5.8l7 4.8 7-4.8V13H1z"/></svg>info@averylane.com</li>
        <li><svg viewBox="0 0 16 16"><path d="M4 1h6l2 2v3H4z M1 6h14v7h-3v2H4v-2H1z M5 10v4h6v-4z"/></svg>5550142739</li>
      </ul>
    </div>
    <p class="copyright">© Copyrights 2023 Avery Lane | All Rights Reserved</p>
    <a class="social" href="#" aria-label="Professional profile"></a>
  </footer>

</div>
</body>
</html>
```